Environmental and Industrial Services Company Needs Brochure Design

We need a new brochure design for an established company that services the Southeastern United States. It is a highly diversified company that centers around Environmental and Industrial Services. The Environmental side revolved around emergency chemical and spill response, HAZMAT, hazardous/ non hazardous waste management, wastewater treatment, and remediation services (cleaning up contaminated sites). And the Industrial side utilizes heavy equipment like vacuum trucks and hydroblasters to clean process equipment inside of factories and manufacturing facilities. Predominantly our clients are large industrial clients, commercial clients, and the government. The people who would see the brochure are decision makers; engineers, project managers, procurement heads for large companies. These are serious and educated people who are looking for the best.

The designs should incorporate our colors and I welcome you to use any of the pictures from our website www.kdlpurex.com EXCLUSIVELY FOR THIS PROJECT, of course. This brochure should communicate professionalism, confidence, stability, and portray the kind of company who efficiently manages complicated issues. Our site gives a better kind of idea of the branding we want to extend into the brochure and I caution any designer to NOT allow the environmental aspect of our company to lead them to design brochures more fitting for Green Tech companies or Alternative Energy.

Target Market(s)

Engineers, Factory Managers, Project Managers, Consultants, Heads of Large Companies, Service Managers

Industry/Entity Type

Industrial

Requirements
Must have
• The brochure must
-Be divided like the services section of our website w/ categories in this order:
-Industrial Services, Waste Management, Remediation Services, Emergency Response, Marine Services, Stormwater Services
-Owing to the large info in these sections, I'd recommend separate pages or tabs
-Incorporate our colors
-Use photos from the site

```html
<!DOCTYPE html>
<html lang="en">
<head>
<meta charset="utf-8">
<title>KDL Purex Environmental — Back Page &amp; Cover Page</title>
<link rel="stylesheet" href="https://fonts.googleapis.com/css2?family=Open+Sans:wght@400;600;700&display=swap">
<style>
  :root {
    --stage-bg: #6f6f6f;
    --page-back: #163848;
    --panel-dark: #0f2734;
    --rule: #6f8c9a;
    --ink-light: #c9d6dc;
    --ink-white: #ffffff;
    --cover-glow: #3a7ea0;
    --cover-mid: #1f5572;
    --cover-edge: #133449;
    --tile-yellow: #e0b553;
    --tile-khaki: #b6a36a;
    --tile-orange: #e39f45;
    --tile-steel: #5e8796;
    --tile-blue: #3f7d9e;
    --tile-sky: #6aa2c0;
    --tile-slate: #4e7d96;
    --tile-grey: #7b95a2;
    --tile-olive: #b79a4a;
  }
  * { margin: 0; padding: 0; box-sizing: border-box; }
  html, body { width: 1200px; height: 900px; overflow: hidden; background: var(--stage-bg); }
  body { font-family: "Open Sans", Arial, sans-serif; }

  .spread {
    position: absolute; left: 45px; top: 228px;
    width: 1113px; height: 444px; display: flex;
  }
  .back-page { position: relative; width: 556px; height: 444px; background: var(--page-back); }
  .cover-page {
    position: relative; width: 557px; height: 444px;
    background: radial-gradient(ellipse 360px 300px at 130px 200px, var(--cover-glow) 0%, var(--cover-mid) 45%, var(--cover-edge) 100%);
    overflow: hidden;
  }

  .contact-panel {
    position: absolute; left: 0; top: 162px; width: 179px; height: 126px;
    background: var(--panel-dark); border: 1px solid var(--rule); border-left: none;
    color: var(--ink-white); text-align: center; font-size: 7.5px; line-height: 10px;
  }
  .contact-panel .brand-name { margin-top: 16px; font-weight: 700; font-size: 11px; line-height: 11px; letter-spacing: .3px; }
  .contact-panel .brand-sub { font-weight: 700; font-size: 7.5px; letter-spacing: .6px; margin-bottom: 10px; }
  .contact-panel .address { margin-bottom: 9px; }
  .contact-panel .phones { margin-bottom: 9px; }
  .contact-panel .phones span { display: inline-block; width: 22px; text-align: left; }

  .disclaimer {
    position: absolute; left: 201px; top: 210px; width: 320px;
    color: var(--ink-light); font-size: 5.6px; line-height: 9px;
  }
  .back-rule { position: absolute; left: 0; top: 293px; width: 556px; height: 1px; background: var(--rule); }

  .tile-grid { position: absolute; left: 0; top: 0; }

  .tagline { position: absolute; color: var(--ink-white); font-weight: 400; letter-spacing: .3px; white-space: nowrap; }
  .tagline .cap { font-size: 19px; }
  .tagline.line-one { right: 368px; top: 155px; font-size: 14px; text-transform: uppercase; }
  .tagline.line-two { left: 175px; top: 178px; font-size: 13px; }
  .tagline.line-three {
    left: 195px; top: 192px; font-size: 14px; text-transform: uppercase;
    background: rgba(15, 39, 52, .75); padding: 2px 8px 2px 6px; border-radius: 3px;
  }

  .cover-brand { position: absolute; left: 26px; top: 390px; display: flex; align-items: center; gap: 7px; color: var(--ink-white); font-weight: 700; }
  .cover-brand .mark { width: 28px; height: 28px; background: var(--ink-white); opacity: .9; }
  .cover-brand .name { font-size: 25px; line-height: 24px; white-space: nowrap; }
  .cover-brand .name small { display: block; font-size: 11.5px; line-height: 13px; letter-spacing: 1px; }
</style>
</head>
<body>
<main class="spread">
  <section class="back-page">
    <div class="contact-panel">
      <p class="brand-name">KDL PUREX</p>
      <p class="brand-sub">ENVIRONMENTAL</p>
      <p class="address">1870 Harbor Road<br>Millbrook,&nbsp;&nbsp;NC&nbsp;&nbsp;28555</p>
      <p class="phones"><span>Phone</span> (555) 014-2273<br><span>Fax</span> (555) 014-2290</p>
      <p class="web">www.kdlpurex.com</p>
    </div>
    <p class="disclaimer">
      A disclaimer is generally any statement intended to specify or delimit the scope of rights and obligations that may be exercised and enforced by parties in a legally recognized relationship. In contrast to other terms for legally operative language, the term disclaimer usually implies situations that involve some level of uncertainty, waiver, or risk.<br>
      A disclaimer may specify mutually agreed and privately arranged terms and conditions as part of a contract; or may specify warnings or expectations to the general public (or some other class of persons) in order to fulfill a duty of care owed to prevent unreasonable risk of harm or injury. Some disclaimers are intended to limit exposure to damages after a harm or injury has already been suffered. Additionally, some kinds of disclaimers may represent a voluntary waiver of a right or obligation that may be owed to the disclaimant.
    </p>
    <div class="back-rule"></div>
  </section>

  <section class="cover-page">
    <svg class="tile-grid" width="557" height="444" viewBox="0 0 557 444">
      <defs>
        <linearGradient id="refinery-tones" x1="0" y1="0" x2="0" y2="1">
          <stop offset="0" stop-color="#e4a23e"/><stop offset=".55" stop-color="#9a6a3a"/><stop offset="1" stop-color="#4c5f6a"/>
        </linearGradient>
        <linearGradient id="hazmat-tones" x1="0" y1="0" x2="0" y2="1">
          <stop offset="0" stop-color="#c9a642"/><stop offset="1" stop-color="#7c6a44"/>
        </linearGradient>
        <linearGradient id="truck-tones" x1="0" y1="0" x2="0" y2="1">
          <stop offset="0" stop-color="#9cc3de"/><stop offset=".6" stop-color="#8c99a0"/><stop offset="1" stop-color="#5f7b4a"/>
        </linearGradient>
        <linearGradient id="blaster-tones" x1="0" y1="0" x2="0" y2="1">
          <stop offset="0" stop-color="#a9c6d6"/><stop offset=".5" stop-color="#9b9a90"/><stop offset="1" stop-color="#6d6a5e"/>
        </linearGradient>
      </defs>

      <g role="img" aria-label="Photo: vacuum truck parked outside a facility">
        <rect x="63" y="29" width="62" height="62" rx="7" fill="url(#truck-tones)"/>
        <rect x="128" y="29" width="62" height="62" rx="7" fill="url(#truck-tones)"/>
      </g>

      <rect x="259" y="29" width="62" height="62" rx="7" fill="var(--tile-yellow)"/>
      <rect x="324" y="29" width="62" height="62" rx="7" fill="var(--tile-khaki)"/>
      <rect x="389" y="29" width="62" height="62" rx="7" fill="var(--tile-orange)"/>
      <rect x="455" y="29" width="62" height="62" rx="7" fill="var(--tile-steel)"/>

      <rect x="128" y="92" width="62" height="62" rx="7" fill="var(--tile-blue)"/>
      <rect x="194" y="92" width="62" height="62" rx="7" fill="var(--tile-olive)"/>

      <g role="img" aria-label="Photo: industrial plant chimneys against a sunset sky">
        <rect x="259" y="92" width="62" height="62" rx="7" fill="url(#refinery-tones)"/>
        <rect x="324" y="92" width="62" height="62" rx="7" fill="url(#refinery-tones)"/>
        <rect x="389" y="92" width="62" height="62" rx="7" fill="url(#refinery-tones)"/>
        <rect x="194" y="156" width="62" height="62" rx="7" fill="#5d6a70"/>
        <rect x="259" y="156" width="62" height="62" rx="7" fill="#6a6e6c"/>
        <rect x="324" y="156" width="62" height="62" rx="7" fill="#5f7a88"/>
      </g>

      <rect x="389" y="156" width="62" height="62" rx="7" fill="var(--tile-sky)"/>

      <g role="img" aria-label="Photo: responders in hazmat suits working on a rusted pipe">
        <rect x="455" y="92" width="62" height="62" rx="7" fill="url(#hazmat-tones)"/>
        <rect x="455" y="156" width="62" height="62" rx="7" fill="url(#hazmat-tones)"/>
      </g>

      <rect x="259" y="219" width="62" height="62" rx="7" fill="var(--tile-sky)"/>
      <rect x="324" y="219" width="62" height="62" rx="7" fill="var(--tile-slate)"/>
      <rect x="389" y="219" width="62" height="62" rx="7" fill="var(--tile-grey)"/>

      <rect x="324" y="283" width="62" height="62" rx="7" fill="var(--tile-slate)"/>
      <rect x="389" y="283" width="62" height="62" rx="7" fill="var(--tile-blue)"/>

      <g role="img" aria-label="Photo: worker hydroblasting equipment at an industrial site">
        <rect x="455" y="283" width="62" height="62" rx="7" fill="url(#blaster-tones)"/>
        <rect x="389" y="346" width="62" height="62" rx="7" fill="#8d8a80"/>
        <rect x="455" y="346" width="62" height="62" rx="7" fill="url(#blaster-tones)"/>
      </g>
    </svg>

    <p class="tagline line-one"><span class="cap">S</span>imple solutions</p>
    <p class="tagline line-two">to</p>
    <p class="tagline line-three"><span class="cap">C</span>omplex problems</p>

    <div class="cover-brand">
      <span class="mark"></span>
      <p class="name">KDL PUREX<small>ENVIRONMENTAL</small></p>
    </div>
  </section>
</main>
</body>
</html>
```